Business Card for Industrial Distributor

We need a business card design for an industrial distributor. We sell machine parts for the manufacturing and oil industry. We would like the cards to look clean and modern but with a touch of industry.

Our colors are blue/white.

Please feel free to visit our website www.korvanlineusa.com

Target Market(s)

mexican manufacturers in the automobile/aerospace industry

Industry/Entity Type

Industrial

Colors
ffffff
0555a3

```html
<!DOCTYPE html>
<html lang="en">
<head>
<meta charset="utf-8">
<title>Korvanline Business Card</title>
<link rel="stylesheet" href="https://fonts.googleapis.com/css2?family=Roboto:wght@400;700&display=swap">
<style>
  :root {
    --page: #eeeeef;
    --navy: #2e3589;
    --blue-deep: #2c3290;
    --blue-bright: #2a6fd2;
    --white: #ffffff;
  }
  * { margin: 0; padding: 0; box-sizing: border-box; }
  html, body { width: 1083px; height: 1200px; overflow: hidden; background: var(--page); }
  body { position: relative; font-family: "Roboto", Arial, sans-serif; }

  .card {
    position: absolute; left: 188px; width: 708px; height: 420px; overflow: hidden;
    box-shadow: 0 6px 16px rgba(0,0,0,0.25);
  }
  .card--front { top: 136px; }
  .card--back { top: 614px; }
  .card__bg { position: absolute; inset: 0; }

  .brand { position: absolute; display: flex; align-items: center; }
  .brand__dot { border-radius: 50%; flex: none; }
  .brand__name { font-weight: 700; letter-spacing: -0.5px; line-height: 1; }

  .card--front .brand { left: 120px; top: 101px; gap: 18px; }
  .card--front .brand__dot { width: 90px; height: 90px; background: var(--navy); }
  .card--front .brand__name { font-size: 74px; color: var(--navy); }

  .gear-decor {
    position: absolute; left: 548px; top: 214px; width: 150px; height: 196px;
    border-radius: 8px;
    background: linear-gradient(180deg, rgba(120,130,190,0.18), rgba(140,150,210,0.28));
  }

  .website {
    position: absolute; left: 0; right: 0; top: 314px; text-align: center;
    color: var(--white); font-weight: 700; font-size: 29px;
  }

  .card--back .brand { left: 0; right: 0; top: 46px; justify-content: center; gap: 10px; }
  .card--back .brand__dot { width: 50px; height: 50px; background: var(--white); }
  .card--back .brand__name { font-size: 42px; color: var(--white); }
  .company { position: absolute; left: 0; right: 0; top: 104px; text-align: center; color: var(--white); font-size: 22px; }

  .person { position: absolute; right: 374px; top: 238px; text-align: right; color: var(--navy); }
  .person__name { font-weight: 700; font-size: 22px; line-height: 1.2; }
  .person__role { font-size: 21px; line-height: 1.3; }
  .divider { position: absolute; left: 353px; top: 220px; width: 2px; height: 98px; background: var(--navy); }

  .contacts { position: absolute; left: 376px; top: 218px; list-style: none; color: var(--navy); font-size: 21px; }
  .contacts li { display: flex; align-items: center; height: 36px; gap: 8px; }
  .contacts svg { width: 22px; height: 22px; flex: none; }

  .address { position: absolute; left: 100px; top: 364px; display: flex; align-items: center; gap: 10px; color: var(--navy); font-size: 21px; }
  .address svg { width: 20px; height: 28px; }
</style>
</head>
<body>

<section class="card card--front">
  <svg class="card__bg" viewBox="0 0 708 420" preserveAspectRatio="none">
    <defs>
      <linearGradient id="silverFront" x1="0" y1="0" x2="1" y2="0.3">
        <stop offset="0" stop-color="#d6d7da"/>
        <stop offset="0.45" stop-color="#ffffff"/>
        <stop offset="1" stop-color="#c8c9cc"/>
      </linearGradient>
      <linearGradient id="bandFront" x1="0" y1="0" x2="0" y2="1">
        <stop offset="0" stop-color="var(--blue-bright)"/>
        <stop offset="0.45" stop-color="var(--blue-deep)"/>
        <stop offset="1" stop-color="var(--navy)"/>
      </linearGradient>
    </defs>
    <rect width="708" height="420" fill="url(#silverFront)"/>
    <path d="M0 262 Q354 240 708 262 L708 420 L0 420 Z" fill="var(--navy)"/>
    <path d="M0 266 Q354 244 708 266 L708 420 L0 420 Z" fill="#b9bbc2"/>
    <path d="M0 276 Q354 256 708 276 L708 420 L0 420 Z" fill="url(#bandFront)"/>
  </svg>
  <div class="gear-decor" role="img" aria-label="Faint gear decoration"></div>
  <div class="brand">
    <span class="brand__dot"></span>
    <span class="brand__name">Korvanline</span>
  </div>
  <p class="website">www.korvanlineusa.com</p>
</section>

<section class="card card--back">
  <svg class="card__bg" viewBox="0 0 708 420" preserveAspectRatio="none">
    <defs>
      <linearGradient id="silverBack" x1="0" y1="0" x2="1" y2="0.3">
        <stop offset="0" stop-color="#d4d5d8"/>
        <stop offset="0.5" stop-color="#ffffff"/>
        <stop offset="1" stop-color="#cacbce"/>
      </linearGradient>
      <linearGradient id="bandBack" x1="0" y1="0" x2="0" y2="1">
        <stop offset="0" stop-color="var(--navy)"/>
        <stop offset="0.55" stop-color="var(--blue-deep)"/>
        <stop offset="1" stop-color="var(--blue-bright)"/>
      </linearGradient>
    </defs>
    <rect width="708" height="420" fill="url(#silverBack)"/>
    <path d="M0 0 H708 V162 Q354 182 0 162 Z" fill="#b9bbc2"/>
    <path d="M0 158 Q354 178 708 158" stroke="var(--navy)" stroke-width="3" fill="none"/>
    <path d="M0 0 H708 V146 Q354 166 0 146 Z" fill="url(#bandBack)"/>
  </svg>
  <div class="brand">
    <span class="brand__dot"></span>
    <span class="brand__name">Korvanline</span>
  </div>
  <p class="company">Korvanline International Corp.</p>

  <div class="person">
    <p class="person__name">YOUR NAME</p>
    <p class="person__role">Position</p>
  </div>
  <span class="divider"></span>

  <ul class="contacts">
    <li>
      <svg viewBox="0 0 24 24" aria-hidden="true"><path d="M7 3 L10 7 L8 10 Q10 14 14 16 L17 14 L21 17 L19 21 Q9 20 4 6 Z" fill="var(--navy)"/></svg>
      <span>(956) 555-0142</span>
    </li>
    <li>
      <svg viewBox="0 0 24 24" aria-hidden="true"><rect x="6" y="3" width="12" height="7" fill="none" stroke="var(--navy)" stroke-width="2"/><rect x="3" y="10" width="18" height="9" rx="1" fill="var(--navy)"/><rect x="7" y="15" width="10" height="6" fill="#fff" stroke="var(--navy)" stroke-width="1.5"/></svg>
      <span>(956) 555-0187</span>
    </li>
    <li>
      <svg viewBox="0 0 24 24" aria-hidden="true"><rect x="3" y="6" width="18" height="12" fill="none" stroke="var(--navy)" stroke-width="2"/><path d="M3 6 L12 13 L21 6" fill="none" stroke="var(--navy)" stroke-width="2"/></svg>
      <span>sales@korvanlineusa.com</span>
    </li>
  </ul>

  <div class="address">
    <svg viewBox="0 0 20 28" aria-hidden="true"><path d="M10 1 A9 9 0 0 1 19 10 Q19 17 10 27 Q1 17 1 10 A9 9 0 0 1 10 1 Z" fill="var(--navy)"/><circle cx="10" cy="10" r="3.5" fill="#fff"/></svg>
    <span>4180 Harbor Mill Rd. Brownsville, TX 78521</span>
  </div>
</section>

</body>
</html>
```